2-sided Postcard Design

We are an artisan chocolate candy company. We are inspired by old world Spanish candies and love to experiment with new and exciting flavor combinations. You can view our current Chatterly/Quippit page for logo and photos @PicoRamaVT. The brochure is for prospective vendors (i.e. grocery/retail stores) who will be carrying our boxed candies.
Updates

Project Deadline Extended
Reason: I'm posting the pics in about an hour- Thanks for your help!

Check the discussions as I have added the things you guys asked for-

Thanks!

Hey there! As you will note the due date has changed (there was a glitch in the system previously). Just for clarification the deadline is indeed Thursday, May 3rd. Looking forward to seeing what you've got!

Thanks!

Target Market(s)

well-traveled adults who enjoy candy, etc.

Industry/Entity Type

It Company

Requirements
Must have
• 2-sided: side #1-logo with company info summary, side #2-menu of items, company offerings, etc.

I attached info regarding the flavors we have featured already. It's just a starting point. It doesn't necessarily need to have all of them listed as add and remove items weekly from the menu. I'd also like to show that we have gluten-free and nut-free options as well as we will be adding sugar free and dairy free candies in the future.

Please also include the following information as well: we use local ingredients where available, we offer new flavors weekly, we make artisan, small batch, hand-dipped candies, we offer personalized flavors as well. Feel free to change wording, etc. as I am not the best when it comes to diction.

I am getting them printed from brelvo.example. Here are their artwork guidelines: http://us.brelvo.example/help/faq/design-overview.html

Also, please include Chatterly and quippit logo and @PicoRamaVT
Nice to have
• 1-2 pictures of product on side #2 (I will upload the pictures 5/2/12), simplistic in design

Should not have
• too much info, graphics, etc.

```html
<!DOCTYPE html>
<html lang="en">
<head>
<meta charset="utf-8">
<title>Pico Rama – Postcard</title>
<link rel="stylesheet" href="https://fonts.googleapis.com/css2?family=Fredoka:wght@600;700&family=Petit+Formal+Script&display=swap">
<style>
  :root {
    --yellow: #fff200;
    --yellow-deep: #f7e21a;
    --pink: #e6197e;
    --black: #141414;
    --white: #ffffff;
    --slate: #2b2b2b;
    --script: "Petit Formal Script", cursive;
    --body: "Fredoka", sans-serif;
  }
  * { margin: 0; padding: 0; box-sizing: border-box; }
  html, body { width: 1200px; height: 850px; overflow: hidden; background: var(--yellow); }
  .postcard { position: relative; width: 1200px; height: 850px; background: var(--yellow); font-family: var(--body); color: var(--black); }

  .side-title { position: absolute; top: 84px; font-family: var(--script); font-size: 29px; font-weight: 400; text-align: center; width: 520px; white-space: nowrap; }
  .side-title--welcome { left: 52px; }
  .side-title--menu { left: 628px; }

  .brand-art { position: absolute; left: 200px; top: 188px; width: 230px; height: 290px;
    background: linear-gradient(180deg, var(--yellow) 0%, var(--yellow-deep) 100%);
    border-radius: 8px; }

  .brand-name { position: absolute; left: 90px; top: 490px; width: 450px; text-align: center; font-weight: 700; font-size: 62px; line-height: 70px; color: var(--pink); }

  .welcome { position: absolute; left: 70px; top: 622px; width: 520px; text-align: center; font-size: 16px; font-weight: 700; line-height: 24.5px; letter-spacing: 0.3px; }
  .accent { color: var(--pink); }

  .flavor { position: absolute; width: 190px; height: 190px; border-radius: 50%; background: var(--black); border: 6px solid var(--pink);
    display: flex; flex-direction: column; align-items: center; justify-content: center; text-align: center; padding: 0 24px; }
  .flavor__name { color: var(--yellow); font-size: 18px; font-weight: 700; line-height: 20px; margin-bottom: 5px; }
  .flavor__desc { color: var(--white); font-size: 12px; font-weight: 700; line-height: 14.5px; }

  .f1 { left: 608px; top: 162px; }
  .f2 { left: 790px; top: 158px; }
  .f3 { left: 976px; top: 160px; }
  .f4 { left: 606px; top: 356px; }
  .f5 { left: 790px; top: 354px; }
  .f6 { left: 980px; top: 352px; }

  .promise { position: absolute; left: 630px; top: 598px; width: 520px; text-align: center; font-size: 16px; font-weight: 700; line-height: 23.5px; letter-spacing: 0.3px; }
  .follow { position: absolute; left: 630px; top: 702px; width: 520px; text-align: center; font-size: 16px; font-weight: 700; color: var(--pink); }

  .social { position: absolute; top: 733px; height: 69px; width: 152px; background: var(--slate); color: var(--white);
    display: flex; flex-direction: column; align-items: center; justify-content: center; }
  .social--chatterly { left: 733px; }
  .social--quippit { left: 889px; }
  .social__name { font-size: 24px; font-weight: 700; line-height: 28px; }
  .social__handle { font-size: 13px; font-weight: 700; }
</style>
</head>
<body>
<main class="postcard">
  <section class="side side--welcome">
    <h1 class="side-title side-title--welcome">Bienvenidos a Pico Rama!</h1>
    <div class="brand-art" role="img" aria-label="Brand mascot illustration"></div>
    <p class="brand-name">Pico Rama</p>
    <p class="welcome">Welcome to <span class="accent">Pico Rama</span> de Santo Varela!<br>
      We are proud to bring you the “<span class="accent">sweetest</span>” thing<br>
      we’ve made yet! <span class="accent">Pico Rama</span> has embraced Old<br>
      World, <span class="accent">traditional</span> candy recipes of the Latinworld<br>
      and added a dash of New World <span class="accent">flavor</span> to bring you<br>
      the delectable tastes of these <span class="accent">yummy treats</span>!</p>
  </section>

  <section class="side side--menu">
    <h2 class="side-title side-title--menu">Candy ingredients</h2>

    <div class="flavor f1"><h3 class="flavor__name">Spicy Peanut Butter Bites</h3><p class="flavor__desc">Creamy peanut butter with a sharp bite covered in dark chocolate</p></div>
    <div class="flavor f2"><h3 class="flavor__name">Tres Gatos Ancho Chile Truffle</h3><p class="flavor__desc">Made with Tres Gatos Ale (Marlow Creek Brewery), ancho chiles, and rich dark chocolate</p></div>
    <div class="flavor f3"><h3 class="flavor__name">Sea-Salted Caramel Chews</h3><p class="flavor__desc">Rich, chewy caramel punctuated with crisp grains of imported sea salt</p></div>
    <div class="flavor f4"><h3 class="flavor__name">Mexican Hot Chocolate Truffles</h3><p class="flavor__desc">Smooth dark chocolate with hints of cinnamon, vanilla, and crème de cacao, rolled in cocoa</p></div>
    <div class="flavor f5"><h3 class="flavor__name">Spicy Key Lime CocoLunas</h3><p class="flavor__desc">Key lime custard with coconut milk and lime zest, in cayenne-spiced dark chocolate</p></div>
    <div class="flavor f6"><h3 class="flavor__name">Mazapanes</h3><p class="flavor__desc">Fresh-made marzipan, hand-dipped in dark chocolate</p></div>

    <p class="promise">We use seasonal local ingredients and keep up-<br>dating new favors weekly! Artisan, small batch,<br>hand-dipped candies, personalized flavors are<br>all available in store!</p>
    <p class="follow">FOLLOW US</p>
    <div class="social social--chatterly"><span class="social__name">Chatterly</span><span class="social__handle">@PicoRamaVT</span></div>
    <div class="social social--quippit"><span class="social__name">Quippit</span><span class="social__handle">@PicoRamaVT</span></div>
  </section>
</main>
</body>
</html>
```